International Perfume distribution Company needs a stationary design

We are a perfume development and distribution company named GLINTO and based in Sao Paulo Brazil. Basically we licence brazilian and international brands and celebrities to develop and distribute its fragrances and perfumes in Brazil. Our current licenced brands are: Varn Colter, Ravena, Delmor Viqueta fragrances and Lara Monteiro (brazilian soap opera celebrity).

We already have our logo and brand that reflects our massive distribution power in Brazil ("spraying our products accross Brazil") and we are also a branch of a big distribution company named BROMAX. It would be nice to mention it in our stationary ("uma divisao do grupo Bromax").

Industry/Entity Type

It Company

Requirements
Must have
• mention that Glinto is a division/branch of bromax using the following phrase: "uma divisão do grupo Bromax"

Use the logo signature: international fragrances

```html
<!DOCTYPE html>
<html lang="pt">
<head>
<meta charset="utf-8">
<title>Glinto – Business Card</title>
<link rel="stylesheet" href="https://fonts.googleapis.com/css2?family=Open+Sans:wght@300;400;700&display=swap">
<style>
  :root {
    --purple: #3a2f8a;
    --orange: #f0a722;
    --ink: #2b2b2b;
    --grey: #5a5a5a;
    --rule: #c9c9c9;
    --paper: #ffffff;
    --backdrop: #e9e7e4;
  }
  * { margin: 0; padding: 0; box-sizing: border-box; }
  html, body { width: 1200px; height: 801px; overflow: hidden; }
  body {
    background: var(--backdrop);
    font-family: "Open Sans", Arial, sans-serif;
    position: relative;
  }
  .card {
    position: absolute;
    top: 246px;
    width: 540px;
    height: 309px;
    background: var(--paper);
    box-shadow: 0 4px 14px rgba(0,0,0,.18);
    overflow: hidden;
  }
  .card--front { left: 30px; }
  .card--back { left: 630px; }

  /* logo lockup */
  .brand {
    display: flex;
    align-items: center;
    gap: 12px;
  }
  .brand__dot {
    border-radius: 50%;
    background: var(--orange);
    flex: none;
  }
  .brand__name {
    color: var(--purple);
    font-weight: 300;
    letter-spacing: 1px;
    line-height: 1;
  }

  /* front */
  .card--front .brand { position: absolute; left: 52px; top: 120px; }
  .card--front .brand__dot { width: 50px; height: 50px; }
  .card--front .brand__name { font-size: 40px; }
  .divider {
    position: absolute;
    left: 296px; top: 22px;
    width: 1px; height: 208px;
    background: linear-gradient(var(--rule), #9d9d9d 60%, var(--rule));
    box-shadow: -3px 0 6px rgba(0,0,0,.08);
  }
  .contact {
    position: absolute;
    left: 312px; top: 24px;
    color: var(--ink);
  }
  .contact__name { font-size: 20px; font-weight: 700; color: var(--purple); line-height: 1.1; }
  .contact__title { font-size: 14px; color: var(--orange); margin-bottom: 12px; }
  .contact__list { list-style: none; font-size: 13.5px; line-height: 20px; }
  .contact__list li { display: flex; align-items: center; gap: 7px; }
  .contact__list li.gap { margin-top: 12px; align-items: flex-start; }
  .contact__list svg { width: 11px; height: 11px; fill: var(--purple); flex: none; }
  .contact__list li.gap svg { margin-top: 4px; }
  .band-line {
    position: absolute; left: 0; right: 0; bottom: 40px;
    height: 2px; background: var(--orange);
  }
  .band {
    position: absolute; left: 0; right: 0; bottom: 0;
    height: 34px; background: var(--purple);
  }

  /* back */
  .card--back .brand { position: absolute; left: 120px; top: 70px; gap: 18px; }
  .card--back .brand__dot { width: 80px; height: 80px; }
  .card--back .brand__name { font-size: 60px; }
  .division {
    position: absolute; left: 0; right: 0; top: 205px;
    text-align: center;
    font-size: 17px; font-weight: 300;
    letter-spacing: 3px; color: var(--grey);
  }
  .web {
    position: absolute; left: 0; right: 0; top: 248px;
    text-align: center;
    font-size: 13px; letter-spacing: 4px; color: var(--ink);
  }
</style>
</head>
<body>

<section class="card card--front" aria-label="Card front">
  <div class="brand">
    <span class="brand__dot"></span>
    <span class="brand__name">GLINTO</span>
  </div>
  <div class="divider"></div>
  <div class="contact">
    <p class="contact__name">Your Name</p>
    <p class="contact__title">Title</p>
    <ul class="contact__list">
      <li><svg viewBox="0 0 12 12"><path d="M2.5 0.5l2 2.5-1 1.3c.7 1.5 1.7 2.5 3.2 3.2l1.3-1 2.5 2-1.2 2.2C4.5 10.5 1.5 7.5.3 1.7z"/></svg>0987 654321</li>
      <li><svg viewBox="0 0 12 12"><path d="M3.5 0h5a1 1 0 0 1 1 1v10a1 1 0 0 1-1 1h-5a1 1 0 0 1-1-1V1a1 1 0 0 1 1-1zm.5 1.5v7.5h4V1.5zM6 10a.6.6 0 1 0 0 1.2.6.6 0 0 0 0-1.2z"/></svg>0987 654321</li>
      <li><svg viewBox="0 0 12 12"><path d="M0 2.5h12v7H0zm1 1v.3l5 3 5-3v-.3z"/></svg>info@glinto.com</li>
      <li><svg viewBox="0 0 12 12"><path d="M6 0a6 6 0 1 0 0 12A6 6 0 0 0 6 0zm0 1c.8 0 1.6 1.7 1.8 4.5H4.2C4.4 2.7 5.2 1 6 1zM1 6.5h2.2c.1 1.5.4 2.8.9 3.7A5 5 0 0 1 1 6.5zm0-1A5 5 0 0 1 4.1 1.8c-.5.9-.8 2.2-.9 3.7zm5 5.5c-.8 0-1.6-1.7-1.8-4.5h3.6C7.6 9.3 6.8 11 6 11zm1.9-.8c.5-.9.8-2.2.9-3.7H11a5 5 0 0 1-3.1 3.7zM8.8 5.5c-.1-1.5-.4-2.8-.9-3.7A5 5 0 0 1 11 5.5z"/></svg>www.glinto.com</li>
      <li class="gap"><svg viewBox="0 0 12 12"><path d="M6 0a4.2 4.2 0 0 0-4.2 4.2C1.8 7.3 6 12 6 12s4.2-4.7 4.2-7.8A4.2 4.2 0 0 0 6 0zm0 6a1.8 1.8 0 1 1 0-3.6A1.8 1.8 0 0 1 6 6z"/></svg><span>00, Complex name<br>City, State 0042</span></li>
    </ul>
  </div>
  <div class="band-line"></div>
  <div class="band"></div>
</section>

<section class="card card--back" aria-label="Card back">
  <div class="brand">
    <span class="brand__dot"></span>
    <span class="brand__name">GLINTO</span>
  </div>
  <p class="division">uma divisão do grupo bromax"</p>
  <p class="web">www.glinto.com</p>
</section>

</body>
</html>
```